An anniversary gift for my girlfriend

My girlfriend and I have been dating for almost 2 years. We met online and this has afforded us the really unique opportunity to have the first words we said to each other (the whole conversation, in fact) preserved. We're moving in together in a few months and she doesn't know that I saved the conversation. I've been waiting for this to turn it into something we can hang in our new place.

The only phrase I want to use is:
"Well if you dislike people's knees then I think we'll get along famously"

It's an Nobody Leaves Before Midnight in Portland reference for the curious.

I want the poster to use the words themselves as the art; I'm thinking typography. I'd like it to match her aesthetic, she likes to wear Nora Vell and T. Brisk. Colors shouldn't be anything too "girly". Somewhere I'd like to include the date June 1, 2015. It shouldn't be a major piece of the poster though, just a way to denote the date.

It should fit (and be fully visible in) a 16x20 (inches) frame

Thanks in advance for the work!

Requirements
Must have
• Must use only the words: "Well if you dislike people's knees then I think we'll get along famously"
• I want this to be typography, so making the phrase the center of the poster and the art itself.

```html
<!DOCTYPE html>
<html lang="en">
<head>
<meta charset="utf-8">
<title>Well, If You Dislike People's Knees — Anniversary Poster</title>
<link rel="stylesheet" href="https://fonts.googleapis.com/css2?family=Open+Sans:ital,wght@0,600;0,700;1,600&family=Montserrat:ital,wght@1,900&family=Alfa+Slab+One&display=swap">
<style>
  :root {
    --plum: #2a0038;
    --navy: #00007a;
    --teal: #0079a0;
    --shadow-red: #ff1a00;
    --band: rgba(170, 20, 40, 0.32);
    --band-dark: rgba(60, 0, 40, 0.22);
    --mint-start: #00a88a;
    --mint-end: #00d36e;
    --lemon: #ffff8a;
    --fuchsia: #e8128c;
    --violet: #8a0a8f;
    --sans: "Open Sans", Arial, sans-serif;
    --heavy: "Montserrat", Arial, sans-serif;
    --slab: "Alfa Slab One", Georgia, serif;
  }
  html, body {
    margin: 0;
    padding: 0;
    overflow: hidden;
    background: #fff;
  }
  .poster {
    position: relative;
    width: 960px;
    height: 1200px;
    overflow: hidden;
  }
  .poster svg {
    display: block;
  }
  .backdrop {
    background: linear-gradient(90deg,
      #f09a6a 0%, #f4c95a 12%, #e8b070 20%, #f3d66a 28%,
      #e6707a 38%, #f2c060 46%, #ee9a9a 54%, #f0c072 62%,
      #e85a5a 72%, #f0d060 82%, #e8c050 90%, #eedc70 100%);
  }
  .phrase-big { font-family: var(--sans); font-weight: 700; }
  .phrase-mid { font-family: var(--sans); font-weight: 700; }
  .phrase-heavy { font-family: var(--heavy); font-weight: 900; font-style: italic; }
  .phrase-italic { font-family: var(--sans); font-weight: 600; font-style: italic; }
  .phrase-slab { font-family: var(--slab); font-weight: 400; }
  .date-mark { font-family: var(--sans); font-weight: 700; }
  .letter-l { fill: var(--plum); }
</style>
</head>
<body>
<main class="poster">
  <svg width="960" height="1200" viewBox="0 0 960 1200" xmlns="http://www.w3.org/2000/svg">
    <defs>
      <linearGradient id="e-fill" gradientUnits="userSpaceOnUse" x1="0" y1="143" x2="0" y2="579">
        <stop offset="0.72" stop-color="var(--navy)"/>
        <stop offset="0.72" stop-color="var(--teal)"/>
      </linearGradient>
      <linearGradient id="mint-fill" x1="0" y1="0" x2="1" y2="0">
        <stop offset="0" stop-color="var(--mint-start)"/>
        <stop offset="1" stop-color="var(--mint-end)"/>
      </linearGradient>
      <linearGradient id="famous-fill" x1="0" y1="0" x2="1" y2="0">
        <stop offset="0" stop-color="var(--fuchsia)"/>
        <stop offset="0.6" stop-color="var(--violet)"/>
        <stop offset="1" stop-color="var(--fuchsia)"/>
      </linearGradient>
    </defs>

    <foreignObject x="0" y="0" width="960" height="1200">
      <div class="backdrop" role="img" aria-label="Painted wooden planks in vertical stripes of orange, yellow, pink and red" style="width:960px;height:1200px"></div>
    </foreignObject>

    <rect class="band-top" x="157" y="68" width="803" height="389" fill="var(--band)"/>
    <rect class="band-bottom" x="357" y="747" width="603" height="189" fill="var(--band-dark)"/>

    <g class="word-well">
      <text class="phrase-big" x="67" y="459" font-size="606" textLength="562" lengthAdjust="spacingAndGlyphs" fill="var(--shadow-red)">W</text>
      <text class="phrase-big" x="50" y="467" font-size="606" textLength="562" lengthAdjust="spacingAndGlyphs" fill="var(--plum)">W</text>
      <text class="phrase-big" x="545" y="562" font-size="610" textLength="241" lengthAdjust="spacingAndGlyphs" fill="var(--shadow-red)">E</text>
      <text class="phrase-big" x="530" y="579" font-size="610" textLength="241" lengthAdjust="spacingAndGlyphs" fill="url(#e-fill)">E</text>
      <path class="letter-l" role="img" aria-label="L" d="M725 482 H764 Q771 482 771 489 V858 H928 Q935 858 935 865 V900 Q935 907 928 907 H724 Q717 907 717 900 V489 Q717 482 725 482 Z"/>
      <path class="letter-l" role="img" aria-label="L" d="M633 700 H678 Q685 700 685 707 V1117 H860 Q867 1117 867 1124 V1164 Q867 1171 860 1171 H632 Q625 1171 625 1164 V707 Q625 700 633 700 Z"/>
    </g>

    <rect class="tag-mint" x="0" y="503" width="510" height="118" fill="url(#mint-fill)"/>
    <text class="phrase-italic" x="15" y="586" font-size="70" textLength="472" lengthAdjust="spacingAndGlyphs" fill="var(--lemon)">IF YOU DISLIKE</text>

    <text class="phrase-mid" x="23" y="692" font-size="62" textLength="608" lengthAdjust="spacingAndGlyphs" fill="var(--plum)">PEOPLE‘S KNEES THEN</text>

    <text class="phrase-heavy" x="75" y="821" font-size="64" textLength="512" lengthAdjust="spacingAndGlyphs" fill="var(--plum)">I THINK WE‘LL</text>
    <text class="phrase-heavy" x="150" y="907" font-size="64" textLength="432" lengthAdjust="spacingAndGlyphs" fill="var(--plum)">GET ALONG</text>

    <text class="phrase-slab" x="18" y="1079" font-size="124" textLength="599" lengthAdjust="spacingAndGlyphs" fill="url(#famous-fill)">FAMOUS</text>
    <text class="phrase-slab" x="697" y="1079" font-size="124" textLength="103" lengthAdjust="spacingAndGlyphs" fill="var(--fuchsia)">Y</text>

    <text class="date-mark" x="700" y="1110" font-size="31" textLength="190" lengthAdjust="spacingAndGlyphs" fill="var(--plum)">June 1, 2015</text>
  </svg>
</main>
</body>
</html>
```